Email Template for AI Website Builder Marketing Campaign

Update: All the designs submitted have too much content for an email template. I have attached a mockup example of a simplified design. Please follow this guideline to revise your design to be less "wordy" and have less content to optimize the delivery rate of the emails. I have also attached the images I used to create the mockup. Feel free to use these images for your revised designs.
Original Brief:
I need a catchy email template for my new AI Website Builder, WebQuilt.ai. The template must be professional, colorful, yet not too complex. The concept of the product is this:
WebQuilt uses Artificial Intelligence (AI) to instantly build stunning websites, absolutely FREE. The user simply specifies their business name and business category (industry), and their stunning new website appears before their eyes!
The template will be used in MailChimp, so please provide the code that I can simply paste into the email body.
Here is a screenshot of our new website (which is not online yet) so you can match the color scheme and style of the email template to the new website design:
https://pixbinstore.com/art_img/7310582/2208634/48165027/9qrt41hwk826zlmpb3nqd7wyex_image.jpg
Let me know if you have any questions.
Thanks!
All submitted designs are too lengthy (too much content) for an email template. I will provide a mockup showing a sample of how you can simplify your design to function better as an email template and better suit my needs. I appreciate your patience!

```html
<!DOCTYPE html>
<html lang="en">
<head>
<meta charset="utf-8">
<title>WebQuilt – Free AI Website Email</title>
<link rel="stylesheet" href="https://fonts.googleapis.com/css2?family=Roboto:wght@300;400;500;700&family=PT+Serif&family=Open+Sans:ital,wght@0,400;0,600;0,700;1,400&display=swap">
<style>
  :root {
    --navy: #0a1a4d;
    --navy-deep: #061338;
    --cyan: #33c6f2;
    --cyan-light: #3fd2f4;
    --blue: #1492f5;
    --white: #ffffff;
    --ink: #3a3a3a;
    --grey-text: #8a8d92;
    --panel-grey: #f4f4f4;
    --heading-navy: #0f1d4d;
  }
  * { box-sizing: border-box; margin: 0; padding: 0; }
  html, body { width: 1200px; height: 2168px; overflow: hidden; background: var(--white); }
  .email { position: relative; width: 1200px; height: 2168px; font-family: "Roboto", Arial, sans-serif; }
  .abs { position: absolute; }

  .hero { position: absolute; left: 0; top: 0; width: 1200px; height: 600px; background: var(--navy); }
  .brand { display: flex; align-items: center; gap: 12px; color: var(--white); font-weight: 700; }
  .brand-mark { width: 48px; height: 48px; background: var(--cyan); border-radius: 4px; }
  .hero .brand { left: 156px; top: 36px; font-size: 30px; letter-spacing: 1px; }
  .forward { left: 848px; top: 42px; display: flex; align-items: center; gap: 8px; color: var(--cyan-light); font-size: 18px; font-weight: 700; }
  .hero-title { left: 152px; top: 186px; color: var(--white); font-weight: 300; }
  .hero-title .line-1 { font-size: 39px; line-height: 48px; }
  .hero-title .accent { color: var(--cyan-light); }
  .hero-title .line-2 { font-size: 50px; line-height: 58px; }
  .hero-title .line-3 { font-size: 42px; line-height: 50px; font-weight: 700; letter-spacing: 1.5px; margin-top: 24px; }

  .btn { display: flex; align-items: center; justify-content: center; border-radius: 40px; color: var(--white); font-weight: 700; background: linear-gradient(90deg, var(--cyan-light), var(--blue)); text-transform: uppercase; }
  .hero .btn { left: 153px; top: 415px; width: 305px; height: 60px; font-size: 18px; }
  .hero-art { left: 712px; top: 120px; width: 356px; height: 442px; border-radius: 40% 30% 20% 30%; background: radial-gradient(ellipse at 45% 45%, #2f7bff 0%, #1740b8 45%, rgba(10,26,77,0) 75%); }

  .wave { position: absolute; left: 0; display: block; }

  .feature-title { left: 152px; top: 786px; width: 460px; font-family: "PT Serif", Georgia, serif; font-size: 42px; line-height: 54px; color: var(--ink); }
  .feature-copy { left: 156px; top: 1022px; width: 450px; font-size: 22px; line-height: 36px; color: var(--grey-text); }
  .feature .btn { left: 157px; top: 1269px; width: 305px; height: 59px; font-size: 18px; }
  .frame-back { left: 672px; top: 817px; width: 396px; height: 459px; border-radius: 6px; background: linear-gradient(135deg, var(--cyan-light), var(--blue)); }
  .frame-art { left: 642px; top: 858px; width: 383px; height: 374px; background: linear-gradient(160deg, #0d2a6e 0%, #0b3c8c 55%, #0e5aa8 100%); border: 1px solid #3fa9e8; }

  .promo { position: absolute; left: 0; top: 1420px; width: 1200px; height: 280px; background: var(--panel-grey); }
  .promo-title { left: 0; top: 1490px; width: 1200px; text-align: center; font-size: 48px; color: var(--heading-navy); }
  .promo .btn, .btn.small { left: 510px; top: 1585px; width: 180px; height: 51px; font-size: 21px; text-transform: none; }

  .footer { position: absolute; left: 0; top: 1780px; width: 1200px; height: 328px; background: var(--navy); font-family: "Open Sans", Arial, sans-serif; color: var(--white); }
  .footer .brand { left: 148px; top: 1833px; font-size: 24px; font-family: "Open Sans", Arial, sans-serif; }
  .footer .brand-mark { width: 40px; height: 40px; }
  .address { left: 148px; top: 1908px; font-family: "Open Sans", Arial, sans-serif; font-size: 19px; line-height: 27px; color: var(--white); }
  .social { left: 148px; top: 2028px; display: flex; gap: 36px; }
  .social span { width: 24px; height: 24px; border-radius: 50%; background: var(--white); display: block; }
  .links { left: 771px; top: 1843px; font-family: "Open Sans", Arial, sans-serif; color: var(--white); }
  .links h3 { font-size: 25px; font-weight: 700; margin-bottom: 22px; }
  .links li { list-style: none; font-size: 19.5px; line-height: 27px; }
  .legal { position: absolute; left: 0; top: 2107px; width: 1200px; height: 61px; background: var(--navy-deep); font-family: "Open Sans", Arial, sans-serif; color: var(--white); font-size: 18px; }
  .legal .copyright { position: absolute; left: 162px; top: 18px; }
  .legal .unsubscribe { position: absolute; right: 150px; top: 18px; font-style: italic; }
</style>
</head>
<body>
<div class="email">
  <section class="hero">
    <div class="abs brand"><span class="brand-mark"></span>WebQuilt</div>
    <div class="abs forward">
      <svg width="20" height="18" viewBox="0 0 20 18" aria-hidden="true"><path d="M12 1 L19 8 L12 15 V10.5 C7 10.5 3.5 12 1 17 C1.5 10 5 6 12 5.5 Z" fill="var(--cyan-light)"/></svg>
      Forward to a friend
    </div>
    <h1 class="abs hero-title">
      <div class="line-1">Your <span class="accent">free</span> stunning website</div>
      <div class="line-2">in one click built by</div>
      <div class="line-3">ARTIFICIAL INTELLIGENCE</div>
    </h1>
    <a class="abs btn">Build my free website</a>
    <div class="abs hero-art" role="img" aria-label="Glowing blue circuit-line illustration of an AI head in profile"></div>
  </section>

  <svg class="wave" style="top:555px" width="1200" height="140" viewBox="0 0 1200 140" aria-hidden="true">
    <rect width="1200" height="140" fill="var(--cyan)"/>
    <path d="M0,0 H1200 V123 C1000,126 800,100 600,70 C400,38 200,10 0,7 Z" fill="var(--navy)"/>
    <path d="M0,52 C200,56 400,76 600,100 C800,124 1000,134 1200,135 V140 H0 Z" fill="var(--white)"/>
  </svg>

  <section class="feature">
    <h2 class="abs feature-title">Harness the power of Artificial Intelliegnce to built your amzing free website today!</h2>
    <p class="abs feature-copy">WebQuilt is the worlds first website builder that builds professional, high-quality websites in seconds! say goodbye to the traditional expensive and time consuming methods of getting your business online!</p>
    <a class="abs btn">Generate free site now</a>
    <div class="abs frame-back"></div>
    <div class="abs frame-art" role="img" aria-label="Laptop showing a generated website, resting above a glowing digital hand"></div>
  </section>

  <section class="promo"></section>
  <h2 class="abs promo-title">Get your free website in second!</h2>
  <a class="abs btn small">Try it Free</a>

  <svg class="wave" style="top:1687px" width="1200" height="100" viewBox="0 0 1200 100" aria-hidden="true">
    <rect width="1200" height="100" fill="var(--navy)"/>
    <path d="M0,0 H1200 V53 C900,45 700,30 500,22 C300,12 150,6 0,5 Z" fill="var(--panel-grey)"/>
    <path d="M0,5 C150,6 300,12 500,22 C700,30 900,45 1200,53 V93 C1000,90 800,75 600,55 C400,35 200,20 0,17 Z" fill="var(--cyan)"/>
  </svg>

  <footer class="footer"></footer>
  <div class="abs brand footer-brand" style="left:148px;top:1833px;font-size:24px;font-family:'Open Sans',Arial,sans-serif;"><span class="brand-mark" style="width:40px;height:40px;"></span>WebQuilt</div>
  <address class="abs address" style="font-style:normal;">WebQuilt 4820<br>Harbor Road, Milford DE 19963</address>
  <div class="abs social" aria-label="Social links"><span></span><span></span><span></span><span></span></div>
  <nav class="abs links">
    <h3>Links</h3>
    <ul>
      <li>Home</li>
      <li>About</li>
      <li>Features</li>
      <li>How it Works</li>
    </ul>
  </nav>
  <div class="legal">
    <span class="copyright">Copyright © WebQuilt 2023, All rights reserved.</span>
    <span class="unsubscribe">unsubscribe</span>
  </div>
</div>
</body>
</html>
```